Ledgerwise Systems Group business card design.

We are a software development company that develop Software for finance companies and related industries.

We need a 2 sided business card designed. We have a new logo already designed (see attached eps and ai) We are after a clean simple corporate look. One side with just our logo, and the second side with our details.

Mark Hollister
Managing Director

Suite 4 Level 9, 138 Kellaway Street Sydney NSW 2000

Direct: +61 2 9374 6021
Mobile: +61 4 2287 5196
Email: markh@lsg-example.net.au
Web: www.lsg-example.net.au

I have included 2 logo files an .ai and .eps. I noticed that the lines either side of the group looks a bit jaggered and needs to be made sharper.

I would like to introduce a little colour somewhere rather than having it all black and white. But not over the top, keeping with a simple clean corporate look. Perhaps a light blue on some of the text?

If you have other ideas would be pleased to review

Regards

Mark H.

```html
<!DOCTYPE html>
<html lang="en">
<head>
<meta charset="utf-8">
<title>Ledgerwise Systems Group — Business Card</title>
<link rel="stylesheet" href="https://fonts.googleapis.com/css2?family=Lato:wght@400;700;900&display=swap">
<style>
  :root {
    --backdrop: #2a2a2a;
    --card: #050505;
    --card-edge: #141414;
    --brand-blue: #3b84d8;
    --brand-blue-deep: #2f6fbd;
    --silver: #bfbfbf;
    --white: #f2f2f2;
    --muted: #cfcfcf;
  }
  * { box-sizing: border-box; margin: 0; padding: 0; }
  html, body { width: 1200px; height: 997px; overflow: hidden; }
  body {
    background: var(--backdrop);
    font-family: "Lato", Arial, sans-serif;
    position: relative;
  }
  .card {
    position: absolute;
    width: 760px;
    height: 420px;
    border-radius: 22px;
    background: linear-gradient(160deg, var(--card-edge), var(--card) 55%);
    overflow: hidden;
    box-shadow: 0 18px 40px rgba(0,0,0,.55);
  }
  .card--front { left: 120px; top: 50px; }
  .card--back  { left: 320px; top: 527px; }

  .band {
    position: absolute; left: 0; right: 0;
    background: linear-gradient(180deg, var(--brand-blue), var(--brand-blue-deep));
  }
  .rule-silver { position: absolute; left: 0; right: 0; height: 7px; background: var(--silver); }

  .card--front .band { top: 0; height: 58px; }
  .card--front .rule-silver { top: 58px; }

  .brand-mark {
    position: absolute; left: 0; right: 0;
    display: flex; align-items: center; justify-content: center; gap: 16px;
  }
  .brand-mark__square { width: 26px; height: 26px; background: var(--brand-blue); }
  .brand-mark__name {
    color: var(--brand-blue);
    font-weight: 900;
    text-transform: uppercase;
    letter-spacing: 2px;
  }
  .card--front .brand-mark { top: 205px; }
  .card--front .brand-mark__name { font-size: 34px; }

  .card--back .band { bottom: 0; height: 96px; display: flex; align-items: center; justify-content: center; }
  .card--back .rule-silver { bottom: 96px; }
  .web {
    color: #e6eef8; font-size: 17px; letter-spacing: 4px;
  }
  .card--back .brand-mark { top: 58px; }
  .card--back .brand-mark__square { width: 18px; height: 18px; }
  .card--back .brand-mark__name { font-size: 22px; }

  .person { position: absolute; left: 70px; top: 190px; text-align: right; width: 290px; }
  .person__name { color: var(--brand-blue); font-weight: 900; font-size: 25px; text-transform: uppercase; letter-spacing: .5px; }
  .person__role { color: var(--muted); font-weight: 700; font-size: 17px; text-transform: uppercase; margin-top: 2px; }

  .divider {
    position: absolute; left: 392px; top: 140px; width: 3px; height: 120px;
    background: linear-gradient(180deg, transparent, var(--brand-blue) 30%, var(--brand-blue) 70%, transparent);
  }

  .contacts { position: absolute; left: 420px; top: 132px; list-style: none; }
  .contacts li { display: flex; align-items: flex-start; gap: 12px; color: var(--white); font-size: 15px; line-height: 1.25; margin-bottom: 11px; }
  .contacts svg { flex: none; width: 20px; height: 20px; }
</style>
</head>
<body>

<section class="card card--front" aria-label="Card front">
  <div class="band"></div>
  <div class="rule-silver"></div>
  <div class="brand-mark">
    <span class="brand-mark__square"></span>
    <span class="brand-mark__name">Ledgerwise Systems Group</span>
  </div>
</section>

<section class="card card--back" aria-label="Card back">
  <div class="brand-mark">
    <span class="brand-mark__square"></span>
    <span class="brand-mark__name">Ledgerwise Systems Group</span>
  </div>

  <div class="person">
    <p class="person__name">Mark Hollister</p>
    <p class="person__role">Managing Director</p>
  </div>

  <div class="divider"></div>

  <ul class="contacts">
    <li>
      <svg viewBox="0 0 20 20" aria-hidden="true"><circle cx="10" cy="10" r="10" fill="#3b84d8"/><path d="M7 5.5l1.6 2.2-1 1.1c.6 1.3 1.5 2.2 2.8 2.8l1.1-1 2.2 1.6-.8 1.7c-3.8-.3-6.8-3.3-7.1-7.1z" fill="#fff"/></svg>
      <span>+61 2 9374 6021</span>
    </li>
    <li>
      <svg viewBox="0 0 20 20" aria-hidden="true"><circle cx="10" cy="10" r="10" fill="#3b84d8"/><rect x="7" y="4.5" width="6" height="11" rx="1" fill="none" stroke="#fff" stroke-width="1.4"/><circle cx="10" cy="13.5" r=".8" fill="#fff"/></svg>
      <span>+61 4 2287 5196</span>
    </li>
    <li>
      <svg viewBox="0 0 20 20" aria-hidden="true"><circle cx="10" cy="10" r="10" fill="#3b84d8"/><rect x="5" y="6.5" width="10" height="7" fill="#fff"/><path d="M5 6.5l5 4 5-4" fill="none" stroke="#3b84d8" stroke-width="1.2"/></svg>
      <span>markh@lsg-example.net.au</span>
    </li>
    <li>
      <svg viewBox="0 0 20 20" aria-hidden="true"><circle cx="10" cy="10" r="10" fill="#3b84d8"/><path d="M10 4a3.8 3.8 0 0 0-3.8 3.8c0 2.9 3.8 7.7 3.8 7.7s3.8-4.8 3.8-7.7A3.8 3.8 0 0 0 10 4z" fill="#fff"/><circle cx="10" cy="7.9" r="1.4" fill="#3b84d8"/></svg>
      <span>Suite 4 Level 9, 138<br>Kellaway Street, Sydney NSW 2000</span>
    </li>
  </ul>

  <div class="rule-silver"></div>
  <div class="band"><span class="web">www.lsg-example.net.au</span></div>
</section>

</body>
</html>
```